Tralven Networks co-marketing flier

We want a flier that our partners (IT consultants) can hand out to their clients and that we can send to local businesses on their behalf to demonstrate that they can help customers purchase a phone system that has professional features that they would expect in a phone solution that costs thousands of dollars.

We want the brochure to look very professional with excellent layout and use of space.

The Tralven Networks corporate colour is green and more details can be found at www.tralvennetworks-example.com.au.

We have attached a draft Word document that contains most of the information we need but please present the information in the way YOU believe it should be laid out.

We are looking for a designer who understands the concept and uses their own skills to produce a work of art.

Target Market(s)

small businesses that want to save money but also want a modern phone with lots of features

Industry/Entity Type

Marketing

Requirements
Must have
• Must have an image of the main phone and a cordless handset to indicate that they don't need wires to set the system up.

Must have our logo and website address

Must have a box or some "placeholder" where our partners can stamp or insert their details.

Must have a "call to action" saying "Contact us for a quote"

```html
<!DOCTYPE html>
<html lang="en">
<head>
<meta charset="utf-8">
<title>Tralven Networks – Phone System Flier</title>
<link href="https://fonts.googleapis.com/css2?family=Arimo:wght@700&family=Michroma&display=swap" rel="stylesheet">
<style>
  :root {
    --green: #2f8f2c;
    --green-bright: #3fa83a;
    --green-deep: #1c5e1a;
    --black: #050505;
    --white: #ffffff;
    --ink: #111111;
    --logo-green: #3a9b3a;
  }
  * { margin: 0; padding: 0; box-sizing: border-box; }
  html, body { width: 848px; height: 1200px; overflow: hidden; background: var(--white); }
  .flier {
    position: relative;
    width: 848px;
    height: 1200px;
    overflow: hidden;
    font-family: "Arimo", Arial, sans-serif;
    font-weight: 700;
    color: var(--white);
  }
  .backdrop { position: absolute; inset: 0; }

  .brand {
    position: absolute;
    left: 62px; top: 62px;
    display: flex; align-items: center; gap: 12px;
    color: var(--logo-green);
    font-size: 34px;
    white-space: nowrap;
  }
  .brand-dot { width: 18px; height: 18px; border-radius: 50%; background: var(--logo-green); }

  .headline {
    position: absolute;
    right: 44px; top: 34px;
    font-family: "Michroma", sans-serif;
    font-weight: 400;
    font-size: 33px;
    line-height: 55px;
    letter-spacing: 3px;
    text-align: right;
    color: var(--ink);
    text-transform: uppercase;
    -webkit-text-stroke: 0.6px var(--ink);
  }

  .product-photo { position: absolute; }
  .desk-phone { left: 45px; top: 140px; width: 335px; height: 170px; border-radius: 14px 40px 10px 10px;
    background: linear-gradient(160deg, #9a9a9a, #3d3d3d 55%, #b5b5b5); }
  .cordless-set { left: 500px; top: 440px; width: 305px; height: 350px; border-radius: 20px;
    background: linear-gradient(160deg, #2a2a2a, #111 60%, #3a3a3a); }

  .tagline {
    position: absolute; color: var(--white); white-space: nowrap;
    -webkit-text-stroke: 1px var(--white);
  }
  .tagline-right { right: 16px; top: 306px; font-size: 41px; letter-spacing: 2.2px; }
  .tagline-left { left: 20px; top: 396px; font-size: 46px; letter-spacing: 3px; }

  .features { position: absolute; left: 60px; top: 520px; font-size: 18px; }
  .features-title { margin-bottom: 3px; line-height: 26px; }
  .feature-list { list-style: none; }
  .feature-list li { display: flex; line-height: 26.6px; white-space: nowrap; }
  .feature-list li::before { content: "\2610"; font-family: Arial, sans-serif; font-weight: 400; width: 70px; }
  .feature-note { display: block; margin-left: -4px; }

  .pitch {
    position: absolute; left: 0; right: 0; top: 812px;
    text-align: center; font-size: 27px; line-height: 40px;
    -webkit-text-stroke: 0.4px var(--white);
  }
  .pitch em { font-style: normal; color: var(--green-bright); -webkit-text-stroke: 0.4px var(--green-bright); }

  .cta {
    position: absolute; left: 12px; top: 963px; font-size: 28px; letter-spacing: 1.6px;
    white-space: nowrap; -webkit-text-stroke: 1px var(--white);
  }
  .company {
    position: absolute; left: 418px; width: 420px; top: 966px;
    font-family: "Michroma", sans-serif; font-weight: 400; font-style: normal;
    font-size: 14px; line-height: 41px; letter-spacing: 2.4px;
    text-align: center; text-transform: uppercase; white-space: nowrap;
    -webkit-text-stroke: 0.4px var(--white);
  }
  .company span { display: block; }
  .company .abn { font-size: 16px; }
  .company .web { font-size: 11px; letter-spacing: 1.4px; }
</style>
</head>
<body>
<main class="flier">
  <svg class="backdrop" width="848" height="1200" viewBox="0 0 848 1200" aria-hidden="true">
    <defs>
      <linearGradient id="paper" x1="0" y1="0" x2="0" y2="1">
        <stop offset="0" stop-color="#ffffff"/>
        <stop offset="1" stop-color="#c4c4c4"/>
      </linearGradient>
      <linearGradient id="band" x1="0" y1="0" x2="0" y2="1">
        <stop offset="0" stop-color="#3aa236"/>
        <stop offset="1" stop-color="#23701f"/>
      </linearGradient>
      <linearGradient id="footer" x1="0" y1="0" x2="0" y2="1">
        <stop offset="0" stop-color="#2f8f2c"/>
        <stop offset="1" stop-color="#9fd19a"/>
      </linearGradient>
    </defs>
    <rect width="848" height="1200" fill="url(#paper)"/>
    <polygon points="435,268 848,268 848,388 468,388 412,478 0,478 0,362 375,362" fill="url(#band)"/>
    <polygon points="474,396 848,396 848,1200 0,1200 0,490 418,490" fill="#050505"/>
    <polygon points="0,1022 380,1022 412,1100 848,1100 848,1200 0,1200" fill="url(#footer)"/>
  </svg>

  <div class="brand"><span class="brand-dot"></span><span>Tralven Networks</span></div>

  <h1 class="headline">Looking<br>for a<br>new phone<br>system?</h1>

  <div class="product-photo desk-phone" role="img" aria-label="Photo of the desk phone with colour display and corded handset"></div>

  <p class="tagline tagline-right">THAN YOU THINK.</p>
  <p class="tagline tagline-left">IT'S CHEAPER</p>

  <section class="features">
    <p class="features-title">Features include, but not limited, to:</p>
    <ul class="feature-list">
      <li>very low line rental rates*</li>
      <li>10c local and national calls untimed</li>
      <li>voicemail-to-email</li>
      <li>Bluetooth-to-mobile</li>
      <li>direct in-dial to every extension</li>
      <li><span>number portability<span class="feature-note">(keep your number when you move)</span></span></li>
      <li>call records via spreadsheet</li>
      <li>flat rate local and national calls</li>
    </ul>
  </section>

  <div class="product-photo cordless-set" role="img" aria-label="Photo of the cordless handset in its charging cradle beside the base station"></div>

  <p class="pitch">Our proven VoIP solution comes with all the<br>professional features to service<br>an office of <em>UP TO 6 PEOPLE</em>.</p>

  <p class="cta">Contact us for a Quote</p>
  <address class="company">
    <span class="name">Kestrel (456 Group Pty Ltd)</span>
    <span class="abn">ABN: 52 317 904 286</span>
    <span class="web">www.tralvennetworks-example.com.au</span>
  </address>
</main>
</body>
</html>
```